Brisk Tide needs a web page for E-commerce site

Small startup business looking for a custom website for my New Saltwater apparel Co.

COMPANY OVERVIEW

Brisk Tide was founded In Mont Belvieu, Tx, right on the heart of pelham cove.

Brisk Tide is the adrenaline, sweat pumping moment you find yourself setting the hook on a monster fish. This is the moment when all your senses come to life as you work to land that trophy, and after a grueling fight when your hi-fiving your fishing buddies...It's that moment... when the waters and the air around you are Brisk Sweet....All or Nothing...pure Addiction......This is BRISK TIDE

Looking for a sharp clean sexy web page for my ecommerce page

I like the look of black background websites.

www.brisktide-demo.com
Updates

I am using shopvane as my host site if that means anything to y'all

Thank you all for the submissions! There were some great ones!  I will have more projects in the future. thanks again

Target Market(s)

inshore/offshore fishing, saltwater enthusiast

Industry/Entity Type

Business

Requirements
Must have
• logo's

inshore/offshore fishing appeal

compatible with shopvane site

```html
<!DOCTYPE html>
<html lang="en">
<head>
<meta charset="utf-8">
<title>Brisk Tide – Ladies Bags</title>
<link rel="stylesheet" href="https://fonts.googleapis.com/css2?family=Ubuntu:wght@300;400&family=Arimo:wght@400&display=swap">
<style>
  :root{
    --sidebar:#151515;
    --sidebar-rule:#3a3a3a;
    --nav-text:#f2f2f2;
    --meta-text:#9a9a9a;
    --accent:#b3161c;
    --tile:#ffffff;
    --hero-light:#c8a888;
    --hero-mid:#8e6f5c;
    --hero-dark:#3f3438;
    --title:#ffffff;
  }
  *{box-sizing:border-box;margin:0;padding:0}
  html,body{width:1200px;height:750px;overflow:hidden;background:#000}
  .page{position:relative;width:1200px;height:750px;overflow:hidden;font-family:'Ubuntu',sans-serif}

  .hero{position:absolute;left:234px;top:0;width:966px;height:750px;
    background:
      radial-gradient(ellipse 40% 35% at 35% 8%, #d9b9a0 0%, transparent 70%),
      radial-gradient(ellipse 45% 60% at 85% 30%, #4a3c40 0%, transparent 70%),
      radial-gradient(ellipse 60% 40% at 55% 85%, #a88c74 0%, transparent 75%),
      linear-gradient(160deg, var(--hero-light) 0%, var(--hero-mid) 55%, var(--hero-dark) 100%);}

  .sidebar{position:absolute;left:0;top:0;width:234px;height:750px;background:var(--sidebar);
    box-shadow:4px 0 10px rgba(0,0,0,.45)}
  .brand{height:141px;border-bottom:1px solid var(--sidebar-rule);display:flex;align-items:center;justify-content:center}
  .brand-name{font-family:'Ubuntu',sans-serif;font-weight:400;font-size:30px;letter-spacing:1px;color:#d8d8d8}

  .main-nav{position:absolute;left:35px;top:168px;list-style:none}
  .main-nav li{font-size:18px;line-height:23.5px;color:var(--nav-text);font-weight:300}

  .account-nav{position:absolute;left:34px;top:330px;list-style:none}
  .account-nav li{font-family:'Arimo',sans-serif;font-size:12px;line-height:17px;color:var(--meta-text);letter-spacing:.3px}

  .search{position:absolute;left:30px;top:479px}
  .search-label{font-size:18px;color:var(--nav-text);font-weight:300;margin-left:5px;margin-bottom:6px}
  .search-field{display:flex;width:169px;height:28px}
  .search-input{flex:1;background:#fff;font-family:'Arimo',sans-serif;font-size:12px;color:#222;padding-left:8px;line-height:28px}
  .search-btn{width:28px;background:var(--accent);display:flex;align-items:center;justify-content:center}

  .social{position:absolute;left:38px;top:627px;display:flex;gap:7px}
  .social span{width:40px;height:40px;border-radius:50%;display:block}
  .social .s1{background:#3f5b95}.social .s2{background:#2a9ad1}.social .s3{background:#e07a3c}

  .footer-note{position:absolute;left:34px;top:684px;font-family:'Arimo',sans-serif;font-size:12px;line-height:15px;color:var(--meta-text)}

  .page-title{position:absolute;left:285px;top:145px;font-size:44px;font-weight:300;color:var(--title);
    text-shadow:1px 2px 3px rgba(0,0,0,.55)}

  .product-grid{position:absolute;left:284px;top:230px;display:grid;grid-template-columns:repeat(4,178px);
    grid-auto-rows:178px;column-gap:19px;row-gap:28px}
  .product-tile{background:var(--tile);box-shadow:2px 3px 6px rgba(0,0,0,.5);display:flex;align-items:center;justify-content:center}
  .product-photo{width:140px;height:130px;border-radius:30px 30px 18px 18px}
  .bag-tan{background:linear-gradient(#d2733a,#a84e20)}
  .bag-brown{background:linear-gradient(#9a5a35,#6e3b20)}
  .bag-gold{background:linear-gradient(#d3b06a,#a7813c)}
  .bag-green{background:linear-gradient(#2aa466,#137a45)}

  .corner-mark{position:absolute;right:34px;bottom:22px;font-size:40px;color:rgba(40,40,40,.45);letter-spacing:1px}
</style>
</head>
<body>
<div class="page">
  <div class="hero" role="img" aria-label="Large lifestyle photo of a woman in a straw hat and knitted top"></div>

  <aside class="sidebar">
    <div class="brand"><span class="brand-name">BRISK TIDE</span></div>
    <ul class="main-nav">
      <li>Home</li>
      <li>Shipping &amp; Returns</li>
      <li>RSS Syndication</li>
      <li>Categories</li>
    </ul>
    <ul class="account-nav">
      <li>My Account</li>
      <li>Order Status</li>
      <li>Wish Lists</li>
      <li>Gift Certificates</li>
      <li>View Cart</li>
      <li>Sign in or Sign up</li>
    </ul>
    <div class="search">
      <div class="search-label">Search</div>
      <div class="search-field">
        <div class="search-input">Find Products</div>
        <div class="search-btn"><svg width="12" height="12" viewBox="0 0 12 12"><path d="M1 1 L11 6 L1 11 Z" fill="#fff"/></svg></div>
      </div>
    </div>
    <div class="social" aria-label="Social links">
      <span class="s1"></span><span class="s2"></span><span class="s3"></span>
    </div>
    <p class="footer-note">All prices are in USD.<br>Copyright 2013<br>Brisk Tide Apperal Co...</p>
  </aside>

  <h1 class="page-title">Ladies Bags</h1>

  <section class="product-grid">
    <div class="product-tile"><div class="product-photo bag-tan" role="img" aria-label="Orange leather shoulder bag"></div></div>
    <div class="product-tile"><div class="product-photo bag-brown" role="img" aria-label="Brown slouchy hobo bag"></div></div>
    <div class="product-tile"><div class="product-photo bag-gold" role="img" aria-label="Gold buckled hobo bag"></div></div>
    <div class="product-tile"><div class="product-photo bag-green" role="img" aria-label="Green handbag with buckles"></div></div>
    <div class="product-tile"><div class="product-photo bag-tan" role="img" aria-label="Orange leather shoulder bag"></div></div>
    <div class="product-tile"><div class="product-photo bag-brown" role="img" aria-label="Brown slouchy hobo bag"></div></div>
    <div class="product-tile"><div class="product-photo bag-gold" role="img" aria-label="Gold buckled hobo bag"></div></div>
    <div class="product-tile"><div class="product-photo bag-green" role="img" aria-label="Green handbag with buckles"></div></div>
  </section>

  <div class="corner-mark">BRISK TIDE</div>
</div>
</body>
</html>
```